Poster for Dance Choreography Workshop

We need a poster for a dance workshop. This workshop is unique in that instead of focusing on dance technique or on classical compositional practices, it teaches participants a toolbox of a collaborative, improvisational methods for generating movement and creating dances.

The workshop is called VERIL (Methods for Exploring Gesture and Dancemaking). Our dance company is Helen Dorsey & Ensemble.

Here is copy:
VERIL (Methods for Exploring Gesture and Dancemaking) is a six-day intensive led by Helen Dorsey & Ensemble in which dancers and choreographers investigate collaborative approaches to choreography. Each day begins with an hour-long presentation during which Helen Dorsey leads discussions on topics related to choreography and collaboration. Following this, Helen Dorsey and VERIL company members teach a variety of practices for collaborative movement-making that merge improvisational skills with contemporary dance technique and physical theater. Using these practices, participants will create miniature compositions in small groups each day. By examining and discussing these creations, participants leave with greater confidence in their creative abilities and a deeper understanding of composition and movement-making.
This intensive, hosted at Whitcombe College in NYC, brings together a wide variety of talented dance artists and provides them with a supportive environment in which to play, learn, experiment and share. The intensive also affords an exciting opportunity for building peer-communities and forging new creative bonds. VERIL’s goal is that all participants leave with fresh perspectives, tools they can immediately use in their own rehearsals, and a better understanding of their own creative processes.

DATES:
June 11—June 16, 2012
10:00am—6:00pm daily
LOCATION:
Department of Dance,
Whitcombe College of
Harrowgate University
4127 Linden Avenue at 82nd
New York, NY 10094
Housing is not available.
Company teachers:
Helen Dorsey
Maribeth Quennell
Owen Patch
Toby Renfield

Special presentation by
Greta L. Fenwick,
Tall Stage Collective

Applications available online at www.helendorseyensemble.org or email veril@verilworks.org.
Application deadline April 1, 2012.

Hello all,

Nice work so far!
Please note that I have high resolution version of the images in the brief available. I did not include them because of the bandwidth of my connection. If you would like some of the images in higher res (5616x3744) let me know and I can provide them.

Best,

Colin

Target Market(s)

College-age and above. Professional dancers.

Industry/Entity Type

Environment

Requirements
Must have
• Poster must be 11x17 or smaller.
Visit www.northernmovementfair.org, www.pkthf.org, www.vlxmotion.org for competitors. Should not be easy to confuse with these.

```html
<!DOCTYPE html>
<html lang="en">
<head>
<meta charset="utf-8">
<title>VERIL — Methods for Exploring Gesture and Dancemaking</title>
<link href="https://fonts.googleapis.com/css2?family=Inter+Tight:wght@300;400;700&display=swap" rel="stylesheet">
<style>
  :root {
    --studio-light: #d9d6d0;
    --studio-mid: #a9a39a;
    --floor: #8f877d;
    --shadow: #4a4540;
    --skin: #c98a72;
    --shorts-yellow: #d6a62a;
    --shorts-grey: #5a5754;
    --ink: #ffffff;
    --title-ink: rgba(255, 255, 255, 0.86);
  }
  * { margin: 0; padding: 0; box-sizing: border-box; }
  html, body { width: 1200px; height: 776px; overflow: hidden; background: var(--studio-mid); }
  .poster {
    position: relative;
    width: 1200px;
    height: 776px;
    overflow: hidden;
    font-family: "Inter Tight", "Helvetica Neue", Arial, sans-serif;
    color: var(--ink);
  }
  .photo {
    position: absolute; inset: 0;
    background:
      radial-gradient(ellipse 150px 260px at 920px 180px, rgba(214,166,42,0.85), rgba(214,166,42,0) 70%),
      radial-gradient(ellipse 200px 170px at 600px 260px, rgba(90,87,84,0.9), rgba(90,87,84,0) 75%),
      radial-gradient(ellipse 330px 380px at 620px 430px, rgba(201,138,114,0.75), rgba(201,138,114,0) 70%),
      radial-gradient(ellipse 160px 320px at 960px 520px, rgba(201,138,114,0.6), rgba(201,138,114,0) 70%),
      linear-gradient(180deg, var(--studio-light) 0%, var(--studio-mid) 30%, var(--floor) 60%, var(--shadow) 100%);
  }
  .photo::after {
    content: ""; position: absolute; inset: 0;
    background: linear-gradient(90deg, rgba(40,36,32,0.35) 0%, rgba(40,36,32,0.1) 60%, rgba(40,36,32,0.3) 100%);
  }
  .title { position: absolute; left: 0; top: 0; width: 870px; height: 390px; }
  .title text { fill: var(--title-ink); font-family: "Inter Tight", "Helvetica Neue", Arial, sans-serif; font-weight: 400; }

  .details { position: absolute; left: 913px; top: 78px; width: 280px; }
  .details h2 { font-size: 20px; font-weight: 700; line-height: 24px; }
  .details p { font-size: 20px; font-weight: 300; line-height: 28px; }
  .details .deadline { font-size: 11px; font-weight: 700; line-height: 14px; }
  .details section { margin-bottom: 24px; }
  .details .dates { margin-bottom: 18px; }

  .description { position: absolute; left: 30px; top: 414px; width: 812px; font-size: 13.6px; line-height: 19.6px; font-weight: 400; }
  .description p + p { margin-top: 19px; }
  .description strong { font-weight: 700; }

  .apply { position: absolute; left: 20px; top: 740px; font-size: 15px; font-weight: 700; }
</style>
</head>
<body>
<main class="poster">
  <div class="photo" role="img" aria-label="Photograph of two barefoot dancers in shorts leaning into each other in a bright studio"></div>

  <svg class="title" viewBox="0 0 870 390" aria-label="Methods for Exploring Gesture and Dancemaking">
    <text x="4" y="98" font-size="128" textLength="690" lengthAdjust="spacingAndGlyphs">METHODS</text>
    <text x="700" y="98" font-size="72" textLength="150" lengthAdjust="spacingAndGlyphs" font-weight="300">FOR</text>
    <text x="2" y="200" font-size="118" textLength="852" lengthAdjust="spacingAndGlyphs">EXPLORING</text>
    <text x="0" y="300" font-size="132" textLength="830" lengthAdjust="spacingAndGlyphs">GESTURE</text>
    <text transform="translate(40 380) rotate(-90)" font-size="34" textLength="80" lengthAdjust="spacingAndGlyphs" font-weight="300">AND</text>
    <text x="46" y="375" font-size="100" textLength="800" lengthAdjust="spacingAndGlyphs">DANCEMAKING</text>
  </svg>

  <aside class="details">
    <section class="dates">
      <h2>DATES:</h2>
      <p>June 11—June 16, 2012<br>10:00am—6:00pm daily</p>
      <p class="deadline">Application deadline April 1, 2012.</p>
    </section>
    <section>
      <h2>LOCATION:</h2>
      <p>Department of Dance,<br>Whitcombe College of<br>Harrowgate University<br>4127 Linden Avenue at 82nd<br>New York, NY 10094<br>Housing is not available.</p>
    </section>
    <section>
      <h2>COMPANY TEACHERS:</h2>
      <p>Helen Dorsey<br>Maribeth Quennell<br>Owen Patch<br>Toby Renfield</p>
    </section>
    <section>
      <h2>Special presentation by</h2>
      <p>Greta L. Fenwick,<br>Tall Stage Collective</p>
    </section>
  </aside>

  <div class="description">
    <p><strong>VERIL (Methods for Exploring Gesture and Dancemaking) is a six-day intensive led by Helen Dorsey &amp; Ensemble</strong> in which dancers and choreographers investigate collaborative approaches to choreography. Each day begins with an hour-long presentation during which Helen Dorsey leads discussions on topics related to choreography and collaboration. Following this, Helen Dorsey and VERIL company members teach a variety of practices for collaborative movement-making that merge improvisational skills with contemporary dance technique and physical theater. Using these practices, participants will create miniature compositions in small groups each day. By examining and discussing these creations, participants leave with greater confidence in their creative abilities and a deeper understanding of composition and movement-making.</p>
    <p>This intensive, hosted at Whitcombe College in NYC, brings together a wide variety of talented dance artists and provides them with a supportive environment in which to play, learn, experiment and share. The intensive also affords an exciting opportunity for building peer-communities and forging new creative bonds. VERIL’s goal is that all participants leave with fresh perspectives, tools they can immediately use in their own rehearsals, and a better understanding of their own creative processes.</p>
  </div>

  <p class="apply">Applications available online at www.helendorseyensemble.org or email veril@verilworks.org.</p>
</main>
</body>
</html>
```